New Business Card Design Project VORASTI-Italy

we are VORASTI-Italy
our company in the market for 3 years we are luxury cosmetic company and its about time for a facelift :)
i will like to have elegant luxurious and unique business card
that will give the person that get it a unique, luxurious and elegant impression
I'm VERY OPEN FOR NEW IDEAS , even duo i add a few files of things that i see on line and i like them

i add my logo as well
my website is VORASTI.COM
(if you would like to see the main style that we have)

Target Market(s)

adult that have money :)

Industry/Entity Type

Business

Contact Information for Business Card

Name - Paul Vorasti
Position - CEO and CO Founder
address - 4817 E Larkdale
telephone - 555-384-1962
email - paul@vorasti.com
fax - 555-384-1962
website - VORASTI.COM

Colors
000000
959595
fbee3e
ffffff

Requirements
Must have
• big logo in GOLD color
• elegant look
• impressive
Nice to have
• not must but maybe classy pattern background
• not must but maybe emblem
• maybe clear plastic business card
Should not have
• colors
• images

```html
<!DOCTYPE html>
<html lang="en">
<head>
<meta charset="UTF-8">
<title>VORASTI Italy – Business Card</title>
<link rel="stylesheet" href="https://fonts.googleapis.com/css2?family=Cinzel:wght@400&family=Open+Sans:wght@400;600&display=swap">
<style>
  :root {
    --backdrop: #2f2724;
    --card-black: #0d0d0d;
    --silver: #959595;
    --silver-light: #b8b8b8;
    --gold: #d9b23a;
    --gold-bright: #fbee3e;
    --white: #ffffff;
  }
  * { margin: 0; padding: 0; box-sizing: border-box; }
  html, body {
    width: 1200px;
    height: 864px;
    overflow: hidden;
    background: var(--backdrop);
  }
  .stage {
    width: 1200px;
    height: 864px;
    display: flex;
    align-items: center;
    justify-content: center;
    gap: 40px;
  }
  .card {
    width: 540px;
    height: 309px;
    background: var(--card-black);
    border-radius: 3px;
    position: relative;
    box-shadow: 0 10px 30px rgba(0,0,0,0.45);
  }

  /* Front side */
  .card-front {
    display: flex;
    flex-direction: column;
    align-items: center;
    justify-content: center;
  }
  .brand-mark {
    width: 74px;
    height: 74px;
    border-radius: 50%;
    border: 3px solid currentColor;
    margin-bottom: 14px;
  }
  .brand-name {
    font-family: "Cinzel", serif;
    font-weight: 400;
    font-size: 44px;
    line-height: 1;
    letter-spacing: 1px;
    text-align: center;
  }
  .brand-name .brand-country {
    display: block;
    font-size: 14px;
    letter-spacing: 2px;
    margin-top: 8px;
  }
  .card-front .brand { color: var(--silver-light); display: flex; flex-direction: column; align-items: center; }
  .front-web {
    font-family: "Open Sans", sans-serif;
    font-size: 13px;
    letter-spacing: 4px;
    color: var(--silver);
    margin-top: 28px;
  }

  /* Back side */
  .card-back {
    display: flex;
    align-items: center;
    padding: 0 34px 0 40px;
  }
  .card-back .brand {
    color: var(--gold);
    display: flex;
    flex-direction: column;
    align-items: center;
    width: 220px;
  }
  .card-back .brand-name { font-size: 38px; }
  .card-back .brand-mark { width: 66px; height: 66px; }
  .divider {
    width: 2px;
    height: 190px;
    margin: 0 26px 0 22px;
    background: linear-gradient(to bottom, transparent, var(--gold), transparent);
  }
  .contact {
    font-family: "Open Sans", sans-serif;
    color: var(--white);
    font-size: 14px;
    line-height: 1.4;
  }
  .contact-name {
    color: var(--gold);
    font-weight: 600;
    font-size: 18px;
    line-height: 1.2;
  }
  .contact-title { margin-bottom: 12px; }
  .contact-address { margin-bottom: 4px; }
  .contact-label { color: var(--gold); }
</style>
</head>
<body>
<main class="stage">
  <section class="card card-front">
    <div class="brand">
      <span class="brand-mark"></span>
      <div class="brand-name">VORASTI<span class="brand-country">ITALY</span></div>
    </div>
    <p class="front-web">www.vorasti.com</p>
  </section>

  <section class="card card-back">
    <div class="brand">
      <span class="brand-mark"></span>
      <div class="brand-name">VORASTI<span class="brand-country">ITALY</span></div>
    </div>
    <span class="divider"></span>
    <div class="contact">
      <p class="contact-name">Paul Vorasti</p>
      <p class="contact-title">CEO &amp; CO Founder</p>
      <p class="contact-address">4817 E Larkdale</p>
      <p><span class="contact-label">P.</span> 555-384-1962</p>
      <p><span class="contact-label">F.</span> 555-384-1962</p>
      <p><span class="contact-label">E.</span> paul@vorasti.com</p>
      <p><span class="contact-label">W.</span> VORASTI.COM</p>
    </div>
  </section>
</main>
</body>
</html>
```